Looking for a cool & simple business-card-design for digital agency

Hi!

We are a web agency that offers Reputation Management, Zorvik & Seo Services and software development. We like cool things, we like innovative styles.

We have uploaded our logo.

Project Deadline Extended Reason: Client does not want any designs with the colorful logo. Please send us submissions ONLY with the blac and white logo. What the client would like to see:1) Back of the card: is a silver logo on a black background2) front of the card with all the data, please use white background and black logo thank you Added Friday, May 8, 2015

Software

```html
<!DOCTYPE html>
<html lang="de">
<head>
<meta charset="utf-8">
<title>Veltrano AG – Visitenkarte</title>
<link rel="stylesheet" href="https://fonts.googleapis.com/css2?family=Didact+Gothic&family=Montserrat:wght@500;700&display=swap">
<style>
  :root {
    --ink: #000000;
    --paper: #ffffff;
    --silver: #b9b9bc;
    --frame: #4a4a4a;
  }
  * { box-sizing: border-box; margin: 0; padding: 0; }
  html, body { width: 1015px; height: 1200px; overflow: hidden; background: var(--paper); }
  .sheet { position: relative; width: 1015px; height: 1200px; }

  .card-back {
    position: absolute; left: 0; top: 0; width: 1015px; height: 577px;
    background: var(--ink);
    display: flex; align-items: center; justify-content: center;
  }
  .brand { display: flex; align-items: center; gap: 22px; font-family: "Montserrat", sans-serif; font-weight: 700; }
  .brand-mark { display: block; background: currentColor; }
  .card-back .brand { color: var(--silver); font-size: 78px; letter-spacing: 2px; }
  .card-back .brand-mark { width: 70px; height: 70px; }

  .card-front {
    position: absolute; left: 0; top: 613px; width: 1015px; height: 578px;
    background: var(--paper); border: 2px solid var(--frame); border-right: none;
  }
  .card-front .brand { position: absolute; left: 48px; top: 44px; color: var(--ink); font-size: 46px; gap: 16px; letter-spacing: 1px; }
  .card-front .brand-mark { width: 46px; height: 46px; }

  .name-band {
    position: absolute; left: 0; top: 154px; width: 100%; height: 58px;
    background: var(--ink); color: var(--paper);
    font-family: "Montserrat", sans-serif; font-weight: 500; font-size: 44px;
    line-height: 58px; padding-left: 50px;
  }

  .contact { position: absolute; left: 0; right: 0; top: 262px; text-align: center; font-family: "Didact Gothic", sans-serif; color: var(--ink); }
  .phone { font-size: 50px; line-height: 64px; letter-spacing: -1.5px; }
  .email { font-size: 52px; line-height: 60px; letter-spacing: -1.5px; }

  .bracket { position: relative; display: inline-block; line-height: 60px; vertical-align: top; }
  .bracket-line {
    position: absolute; left: 0; right: 0; bottom: var(--drop); height: var(--depth);
    border: 3px solid var(--ink); border-top: none; border-radius: 0 0 12px 12px;
  }
  .bracket-label {
    position: absolute; left: 50%; transform: translateX(-50%); bottom: calc(var(--drop) + 5px);
    font-size: 24px; letter-spacing: 0; line-height: 24px; white-space: nowrap;
  }
  .bracket-email { --drop: -125px; --depth: 140px; }
  .bracket-site { --drop: -79px; --depth: 93px; }
  .bracket-domain { display: inline-block; position: relative; line-height: 60px; vertical-align: top; }
  .bracket-handle { position: absolute; top: 0; bottom: 0; left: -0.55em; right: 0; --drop: -32px; --depth: 46px; }
</style>
</head>
<body>
<main class="sheet">
  <section class="card-back">
    <div class="brand"><span class="brand-mark"></span><span class="brand-name">Veltrano AG</span></div>
  </section>

  <section class="card-front">
    <div class="brand"><span class="brand-mark"></span><span class="brand-name">Veltrano AG</span></div>
    <div class="name-band">MARC Delling</div>
    <div class="contact">
      <p class="phone">5550 19284</p>
      <p class="email"><span class="bracket bracket-email">info@<span class="bracket bracket-site"><span class="bracket-domain">veltRANO<span class="bracket-handle"><span class="bracket-line"></span><span class="bracket-label">twitter</span></span></span>.com<span class="bracket-line"></span><span class="bracket-label">website</span></span><span class="bracket-line"></span><span class="bracket-label">email</span></span></p>
    </div>
  </section>
</main>
</body>
</html>
```